FotoVELTA buisnesscard

Hey :) I need a modern buisnesscard for my company FotoVELTA
It most have:
Dagligleder og Fotograf: Henrik Torvald Bjelland

Mob: +4791642058
Epost: post@fotovelta.no
Adresse: Bakkestien22, 6099 Fjellbrekka

Facbook and instagram logo with text FotoVELTA

FotoVELTA logo

It Company

```html
<!DOCTYPE html>
<html lang="no">
<head>
<meta charset="utf-8">
<title>FotoVELTA – visittkort</title>
<link rel="stylesheet" href="https://fonts.googleapis.com/css2?family=Arimo:wght@400;700&display=swap">
<style>
  :root {
    --backdrop: #efedec;
    --card: #ffffff;
    --ink: #111111;
    --icon-ring: #6f6f6f;
    --card-edge: #dddddd;
  }
  * { margin: 0; padding: 0; box-sizing: border-box; }
  html, body {
    width: 1200px;
    height: 800px;
    overflow: hidden;
    background: var(--backdrop);
    font-family: "Arimo", Arial, sans-serif;
    color: var(--ink);
  }
  .sheet {
    position: relative;
    width: 1200px;
    height: 800px;
  }
  .card {
    position: absolute;
    top: 281px;
    width: 430px;
    height: 238px;
    background: var(--card);
    border: 1px solid var(--card-edge);
    overflow: hidden;
  }
  .card--back { left: 110px; }
  .card--front { left: 639px; }

  /* Back face: company name top and bottom, centred */
  .back-name {
    position: absolute;
    left: 0;
    right: 0;
    text-align: center;
    font-weight: 700;
    font-size: 44px;
    letter-spacing: 0.5px;
    line-height: 1;
  }
  .back-name--top { top: 8px; }
  .back-name--bottom { bottom: 8px; }

  /* Front face */
  .social {
    position: absolute;
    top: 19px;
    left: 20px;
    display: flex;
    gap: 6px;
  }
  .social__ring {
    width: 32px;
    height: 32px;
    border: 1.5px solid var(--icon-ring);
    border-radius: 50%;
  }
  .brand-name {
    position: absolute;
    top: 58px;
    right: 19px;
    font-weight: 700;
    font-size: 18px;
    letter-spacing: 0.2px;
    line-height: 1;
  }
  .divider {
    position: absolute;
    top: 109px;
    left: 20px;
    width: 391px;
    height: 4px;
    background: var(--ink);
  }
  .person {
    position: absolute;
    top: 127px;
    left: 21px;
    font-size: 14px;
    letter-spacing: 1.2px;
    line-height: 16px;
  }
  .contact {
    position: absolute;
    font-size: 12.5px;
    letter-spacing: 1.1px;
    line-height: 16px;
    font-style: normal;
  }
  .contact--address { left: 47px; top: 178px; }
  .contact--reach { left: 242px; top: 176px; }
</style>
</head>
<body>
  <main class="sheet">
    <section class="card card--back" aria-label="Visittkort, bakside">
      <p class="back-name back-name--top">FotoVELTA</p>
      <p class="back-name back-name--bottom">FotoVELTA</p>
    </section>

    <section class="card card--front" aria-label="Visittkort, forside">
      <div class="social" aria-label="Sosiale medier">
        <span class="social__ring"></span>
        <span class="social__ring"></span>
      </div>
      <p class="brand-name">FotoVELTA</p>
      <div class="divider"></div>
      <p class="person">Henrik Torvald Bjelland<br>Dagligleder og Fotograf</p>
      <address class="contact contact--address">Bakkestien22<br>6099 Fjellbrekka</address>
      <address class="contact contact--reach">+ 47.91.64.20.58<br>post@fotovelta.no</address>
    </section>
  </main>
</body>
</html>
```